Design a Flooring flyer based on out information

We are a flooring company who specialise in supply & installation of high quality flooring (Laminate, SPC vinyl planks and engineered timber)

The colours in flyer should only consist the same colours in business logo as attached

Flyer needs to show customers we offer samples for free delivered to see quality and colours. This can only be ordered via our website.

Contact number: 1300 482 915

www.breltonsflooringsolutions.com.au

instagram: breltonssolutionsgroup

Inregards to texts for flyer.. I will attach our body content of 'about us' Please add some key points in flyer

About Us

Marcus Brelton founded Brelton’s Flooring Solutions with one goal in mind – quality flooring equipment. Our team is made up of flooring professionals who have had extensive experience with flooring installation themselves. Therefore, we are experts at equipping customers with the right products they need to succeed.

The team at Brelton’s Flooring Solutions have had mastered all sorts of flooring technology as we are always focused on innovation and advancement. For example, our expert team has mastered the correct click system that floors need to be suitable for water spills, surface scratches, and foot traffic impact. This is just one of the ways our hands-on team strives to provide our customers with the innovative flooring technology.

Additionally, we make sure that our products are specifically suited to flourish in the Australian environment, and all of our equipment have been approved by Australian standards. Rain, drought or shine, our products are built to survive in Australian weather.

At Brelton’s Flooring Solutions, we work with you to ensure the best outcome for your unique situation. Just contact our friendly and knowledgeable team today to find out more.

Target Market(s)

Home owners

Requirements
Must have
• Logo colours, modern and expensive

```html
<!DOCTYPE html>
<html lang="en">
<head>
<meta charset="utf-8">
<title>Brelton’s Flooring Solutions – Flyer</title>
<link href="https://fonts.googleapis.com/css2?family=Rubik:wght@400;500;700&family=Open+Sans:wght@400;600&family=Montserrat:wght@500;600&display=swap" rel="stylesheet">
<style>
  :root{
    --green:#6cb52d;
    --green-light:#8dc63f;
    --charcoal:#444446;
    --charcoal-dark:#38383a;
    --ink:#3a3a3c;
    --white:#ffffff;
    --wood:#a85a26;
    --wood-light:#c98a52;
    --wall:#ece8e2;
  }
  *{margin:0;padding:0;box-sizing:border-box}
  html,body{width:720px;height:1200px;overflow:hidden;background:var(--white)}
  .flyer{position:relative;width:720px;height:1200px;overflow:hidden;background:var(--white);font-family:"Open Sans",sans-serif;color:var(--ink)}
  .shapes{position:absolute;inset:0}
  .photo{position:absolute}
  .hero-photo{left:0;top:0;width:720px;height:600px;clip-path:polygon(195px 0,720px 0,720px 560px,551px 388px);
    background:linear-gradient(160deg,var(--wall) 0%,#f4f1ec 35%,var(--wood-light) 55%,var(--wood) 80%,#8a4418 100%)}
  .thumb{background:linear-gradient(150deg,#d9d4cc 0%,#9b8a78 50%,var(--wood) 100%)}
  .thumb-one{left:46px;top:472px;width:176px;height:171px;clip-path:polygon(0 16px,100% 0,100% 100%,0 100%)}
  .thumb-two{left:236px;top:423px;width:176px;height:176px;clip-path:polygon(0 26px,100% 0,100% 88%,0 100%)}
  .thumb-three{left:424px;top:384px;width:177px;height:180px;clip-path:polygon(0 0,100% 0,100% 88%,0 100%);
    background:linear-gradient(160deg,#6b6b6b 0%,#bdb6ac 55%,#d8d2c8 100%)}
  .work-photo{left:0;top:1037px;width:400px;height:163px;clip-path:polygon(0 0,128px 0,400px 163px,0 163px);
    background:linear-gradient(140deg,#8a6a4a 0%,#3e3a36 50%,#a27a56 100%)}

  .brand{position:absolute;left:46px;top:48px;display:flex;flex-direction:column;align-items:flex-start}
  .brand-square{width:64px;height:64px;background:var(--charcoal);margin-bottom:16px}
  .brand-name{font-family:"Rubik",sans-serif;font-weight:700;font-size:23px;line-height:28px;color:var(--charcoal)}

  .headline{position:absolute;left:46px;top:254px;font-family:"Rubik",sans-serif;font-weight:700;font-size:33px;line-height:40px;color:var(--charcoal);text-transform:uppercase}
  .headline .accent{color:var(--green)}
  .range{position:absolute;left:46px;top:386px;font-family:"Rubik",sans-serif;font-weight:400;font-size:21px;line-height:26px;color:var(--ink)}

  .section-title{position:absolute;font-family:"Rubik",sans-serif;font-weight:700;font-size:28px;color:var(--green);text-transform:uppercase}
  .about-title{left:46px;top:652px}
  .about-body{position:absolute;left:46px;top:698px;width:306px;font-size:9.4px;line-height:15.2px;color:#e8e8e8}
  .about-body p{margin-bottom:10px}
  .divider{position:absolute;left:364px;top:600px;width:1.5px;height:459px;background:var(--green)}

  .services-title{left:389px;top:603px}
  .services{position:absolute;left:389px;top:652px;list-style:none}
  .services li{display:flex;align-items:center;height:46px;font-family:"Montserrat",sans-serif;font-weight:500;font-size:29px;color:var(--white)}
  .services svg{width:34px;height:34px;margin-right:20px;flex:none}

  .offer-tag{position:absolute;left:389px;top:820px;width:218px;height:42px;background:var(--green);clip-path:polygon(0 0,170px 0,218px 100%,0 100%);
    font-family:"Rubik",sans-serif;font-weight:700;font-size:31px;line-height:42px;color:var(--charcoal);padding-left:14px}
  .offer-text{position:absolute;left:389px;top:877px;font-family:"Rubik",sans-serif;font-weight:700;font-size:21px;line-height:31px;color:var(--white)}
  .offer-note{position:absolute;left:389px;top:949px;font-family:"Rubik",sans-serif;font-weight:700;font-size:21px;line-height:31px;color:var(--green-light)}

  .contact{position:absolute;left:382px;top:1072px;list-style:none;color:var(--charcoal-dark)}
  .contact li{display:flex;align-items:center;font-family:"Montserrat",sans-serif;font-weight:600}
  .contact svg{flex:none;margin-right:10px}
  .contact .phone{font-size:33px;height:46px;font-weight:500}
  .contact .web,.contact .social{font-size:17px;height:35px}
</style>
</head>
<body>
<main class="flyer">
  <svg class="shapes" width="720" height="1200" viewBox="0 0 720 1200" aria-hidden="true">
    <defs>
      <linearGradient id="fade" x1="0" y1="0" x2="1" y2="0.6">
        <stop offset="0" stop-color="#ffffff"/>
        <stop offset="0.55" stop-color="#f3f8ec"/>
        <stop offset="1" stop-color="#a9d372"/>
      </linearGradient>
    </defs>
    <polygon points="0,535 601,388 720,388 720,1200 0,1200" fill="var(--charcoal)"/>
    <polygon points="601,420 720,520 720,580" fill="var(--green)"/>
    <polygon points="250,1200 720,1200 720,978 380,1090" fill="var(--green)"/>
    <polygon points="330,1125 720,1015 720,978 380,1090" fill="var(--green-light)"/>
  </svg>

  <div class="photo hero-photo" role="img" aria-label="Bright bathroom with freestanding bath and warm timber flooring"></div>
  <svg class="shapes" width="720" height="1200" viewBox="0 0 720 1200" aria-hidden="true">
    <polygon points="195,0 551,388 0,535 0,0" fill="url(#fade)"/>
  </svg>

  <div class="photo thumb thumb-one" role="img" aria-label="Installer laying timber planks in a living room"></div>
  <div class="photo thumb thumb-two" role="img" aria-label="Installer cutting boards with a power saw on site"></div>
  <div class="photo thumb thumb-three" role="img" aria-label="Installer levelling a concrete floor"></div>
  <div class="photo work-photo" role="img" aria-label="Installer kneeling while fitting flooring near a doorway"></div>

  <div class="brand">
    <div class="brand-square"></div>
    <div class="brand-name">Brelton’s Flooring<br>Solutions</div>
  </div>

  <h1 class="headline">Specialise in supply<br>&amp; installation of<br><span class="accent">High quality flooring</span></h1>
  <p class="range">(Laminate, SPC vinyl planks and<br>engineered timber)</p>

  <h2 class="section-title about-title">About us</h2>
  <div class="about-body">
    <p>Marcus Brelton founded Brelton’s Flooring Solutions with one goal in mind – quality flooring equipment. Our team is made up of flooring professionals who have had extensive experience with flooring installation themselves. Therefore, we are experts at equipping customers with the right products they need to succeed.</p>
    <p>The team at Brelton’s Flooring Solutions have had mastered all sorts of flooring technology as we are always focused on innovation and advancement. For example, our expert team has mastered the correct click system that floors need to be suitable for water spills, surface scratches, and foot traffic impact. This is just one of the ways our hands-on team strives to provide our customers with the innovative flooring technology.</p>
    <p>Additionally, we make sure that our products are specifically suited to flourish in the Australian environment, and all of our equipment have been approved by Australian standards. Rain, drought or shine, our products are built to survive in Australian weather.</p>
    <p>At Brelton’s Flooring Solutions, we work with you to ensure the best outcome for your unique situation. Just contact our friendly and knowledgeable team today to find out more.</p>
  </div>

  <div class="divider"></div>

  <h2 class="section-title services-title">Our services</h2>
  <ul class="services">
    <li><svg viewBox="0 0 34 34" aria-hidden="true"><circle cx="17" cy="17" r="16" fill="var(--green)"/><path d="M10 22 L22 10 M13 24 L24 13" stroke="#fff" stroke-width="3" stroke-linecap="round"/></svg>Carpentry</li>
    <li><svg viewBox="0 0 34 34" aria-hidden="true"><circle cx="17" cy="17" r="16" fill="var(--green)"/><g fill="#fff"><rect x="9" y="10" width="7" height="4"/><rect x="18" y="10" width="7" height="4"/><rect x="9" y="15.5" width="7" height="4"/><rect x="18" y="15.5" width="7" height="4"/><rect x="9" y="21" width="7" height="4"/><rect x="18" y="21" width="7" height="4"/></g></svg>Flooring</li>
    <li><svg viewBox="0 0 34 34" aria-hidden="true"><circle cx="17" cy="17" r="16" fill="var(--green)"/><rect x="10.5" y="10.5" width="13" height="13" fill="none" stroke="#fff" stroke-width="2.5" transform="rotate(45 17 17)"/><path d="M12 17 H22" stroke="#fff" stroke-width="2.5"/></svg>Floor levelling</li>
  </ul>

  <div class="offer-tag">We offer</div>
  <p class="offer-text">Samples for free delivered<br>to see quality and colours.</p>
  <p class="offer-note">This can only be ordered<br>via our website.</p>

  <ul class="contact">
    <li class="phone"><svg width="24" height="24" viewBox="0 0 24 24" aria-hidden="true"><circle cx="12" cy="12" r="12" fill="var(--charcoal-dark)"/><path d="M8 6.5c1-.6 1.6.2 2.2 1.4.4.8.2 1.3-.5 1.8.5 1.6 1.5 2.7 3 3.4.6-.7 1.1-.9 1.9-.4 1.2.7 1.9 1.3 1.2 2.2-1 1.4-2.6 1.4-4.6.1C8.8 13.4 6.6 8.9 8 6.5z" fill="var(--green)"/></svg>1300 482 915</li>
    <li class="web"><svg width="22" height="22" viewBox="0 0 22 22" aria-hidden="true"><circle cx="11" cy="11" r="11" fill="var(--charcoal-dark)"/><circle cx="11" cy="11" r="6" fill="none" stroke="var(--green)" stroke-width="1.6"/><path d="M5 11 H17 M11 5 C8 8 8 14 11 17 C14 14 14 8 11 5" fill="none" stroke="var(--green)" stroke-width="1.4"/></svg>breltonsflooringsolutions.com.au</li>
    <li class="social"><svg width="22" height="22" viewBox="0 0 22 22" aria-hidden="true"><circle cx="11" cy="11" r="11" fill="var(--charcoal-dark)"/></svg>breltonssolutionsgroup</li>
  </ul>
</main>
</body>
</html>
```